Prosthetic Brochure

Looking for a trifold brochure that highlights our Prosthetic department. Has to have good stock pictures of prosthetic care. Should have Prosthetic Services from our website www.kelvramedworks.com I would like it in the same colors of our website.

Target Market(s)

Patients and physicians

Industry/Entity Type

Medical

Requirements
Must have
• Pictures of people helping prosthetic patients and information from the flyer I uploaded and our website under Prosthetic services.
Nice to have
• Same color scheme as our website. Blue with orange highlights
Should not have
• Just prosthetics no pictures of braces ( orthotics)

```html
<!DOCTYPE html>
<html lang="en">
<head>
<meta charset="utf-8">
<title>Kelvra MedWorks – Prosthetic Team Brochure</title>
<link href="https://fonts.googleapis.com/css2?family=Montserrat:wght@600;700;800&family=Open+Sans:wght@400;600;700&display=swap" rel="stylesheet">
<style>
:root{
  --navy:#1c3a6e;
  --navy-deep:#132b55;
  --orange:#ec7a2a;
  --white:#ffffff;
  --ink:#2b3448;
  --muted:#5d6678;
  --paper:#eceef1;
  --sky:#dfe8f4;
}
*{box-sizing:border-box;margin:0;padding:0}
html,body{width:1200px;height:4000px;overflow:hidden}
body{background:var(--paper);font-family:"Open Sans",Arial,sans-serif;color:var(--ink);position:relative}
.spread{position:absolute;left:50px;width:1100px;height:820px;display:grid;grid-template-columns:repeat(3,1fr);box-shadow:0 10px 30px rgba(0,0,0,.18);overflow:hidden;background:var(--white)}
.spread--outside{top:1000px}
.spread--inside{top:2200px}
.panel{position:relative;overflow:hidden;padding:28px 26px}
.panel--white{background:var(--white)}
.panel--navy{background:var(--navy);color:var(--white)}
.wave{position:absolute;left:0;bottom:0;width:100%;height:110px}
.photo{border-radius:2px}

/* outside – intro panel */
.brand{display:flex;flex-direction:column;align-items:center;gap:8px;margin-bottom:22px}
.brand__circle{width:92px;height:92px;border-radius:50%;background:var(--navy)}
.brand__name{font-family:"Open Sans",Arial,sans-serif;font-weight:700;font-size:17px;color:var(--navy)}
.intro p{font-size:13px;line-height:1.55;margin-bottom:12px;color:var(--ink)}
.intro .team-row{height:190px;margin:8px -26px 0;background:linear-gradient(180deg,#f3f5f8 0%,#bfd0e6 55%,#6d8fbd 100%)}

/* locations */
.locations__title{font-family:Montserrat,Arial,sans-serif;font-weight:800;color:var(--orange);font-size:24px;letter-spacing:1px;margin:10px 0 22px 12px}
.location{display:flex;gap:12px;margin-bottom:24px;padding-left:12px}
.location svg{flex:none;width:20px;height:26px;margin-top:2px}
.location__addr{font-size:13px;line-height:1.45}
.location__phone{display:inline-block;margin-top:6px;background:var(--orange);color:var(--white);font-weight:700;font-size:12px;padding:3px 10px;border-radius:10px}

/* cover */
.cover{padding:0}
.cover__brand{background:var(--white);padding:24px 0 16px;text-align:center}
.cover__brand .brand__name{font-size:18px}
.cover__band{background:var(--navy);color:var(--white);text-align:center;padding:12px 20px;font-family:Montserrat,Arial,sans-serif;font-weight:700;font-size:16px;line-height:1.3}
.cover__band em{font-style:normal;color:var(--orange)}
.cover__photo{height:330px;background:linear-gradient(160deg,#cfd9e6 0%,#8ea7c7 45%,#3e5f8f 100%)}
.cover__body{position:absolute;left:0;right:0;bottom:0;height:300px;background:var(--navy-deep);padding:40px 28px 0;text-align:center;color:var(--white)}
.cover__swoosh{position:absolute;left:0;top:-40px;width:100%;height:60px}
.cover__title{font-family:Montserrat,Arial,sans-serif;font-weight:800;font-size:40px;line-height:1.08;margin-top:20px}
.cover__title span{color:var(--orange)}
.cover__url{display:inline-block;margin-top:40px;color:var(--orange);font-weight:700;font-size:15px;border-top:2px solid var(--orange);padding-top:8px}

/* inside – why panel */
.why__title{font-family:Montserrat,Arial,sans-serif;font-weight:800;color:var(--navy);font-size:20px;padding-bottom:8px;border-bottom:3px solid var(--orange);margin-bottom:16px}
.why__list{list-style:none}
.why__list li{display:flex;gap:10px;font-size:12px;line-height:1.45;margin-bottom:11px}
.why__list svg{flex:none;width:16px;height:16px;margin-top:2px}
.why__list b{color:var(--navy)}
.why__summary{text-align:center;color:var(--orange);font-weight:700;font-size:13px;margin:14px 10px 16px}
.callbox{display:flex;align-items:center;gap:12px;border:2px solid var(--navy);border-radius:30px;padding:8px 16px 8px 8px}
.callbox__icon{flex:none;width:46px;height:46px;border-radius:50%;background:var(--orange);display:flex;align-items:center;justify-content:center}
.callbox__text{font-size:13px;line-height:1.3;color:var(--navy)}
.callbox__text b{font-family:Montserrat,Arial,sans-serif;font-size:16px}
.why__phone{position:absolute;left:0;right:0;bottom:22px;text-align:center;color:var(--white);font-family:Montserrat,Arial,sans-serif;font-weight:800;font-size:24px;z-index:1}

/* team */
.member{display:flex;gap:14px;align-items:flex-start;margin-bottom:20px}
.member--flip{flex-direction:row-reverse}
.member__photo{flex:none;width:92px;height:106px;background:linear-gradient(180deg,#c9d4e3,#7b93b6)}
.member__name{font-family:Montserrat,Arial,sans-serif;font-weight:700;font-size:11.5px;color:var(--orange);text-transform:uppercase;line-height:1.3;margin-bottom:4px}
.member__bio{font-size:11px;line-height:1.45;color:#dfe6f2}
.partner__title{font-family:Montserrat,Arial,sans-serif;font-weight:800;font-size:14px;color:var(--orange);margin:6px 0 6px}
.partner{display:flex;gap:12px}
.partner p{font-size:11px;line-height:1.45;color:#dfe6f2}
.partner__image{flex:none;width:96px;height:170px;background:linear-gradient(180deg,#e6ebf2,#9fb0c8)}
</style>
</head>
<body>

<section class="spread spread--outside" aria-label="Brochure outside">
  <div class="panel panel--white intro">
    <div class="brand"><span class="brand__circle"></span><span class="brand__name">Kelvra MedWorks</span></div>
    <p>Kelvra MedWorks has been providing quality, compassionate care to residents of St. Louis and Southern Illinois since 1983.</p>
    <p>A recognized leader in the field, our experts work as a team to create the most functional solution to your prosthetic needs using the latest technology available.</p>
    <p>Our patient-centered, team approach means we work closely with your doctor, nurse, therapist and family to deliver a great fitting prosthetic device that works for you.</p>
    <div class="team-row photo" role="img" aria-label="Photo of the prosthetic team standing in a row in scrubs and clinic wear"></div>
    <svg class="wave" viewBox="0 0 367 110" preserveAspectRatio="none"><path d="M0 40 Q180 0 367 30 V110 H0Z" fill="var(--orange)"/><path d="M0 54 Q180 16 367 44 V110 H0Z" fill="var(--navy)"/></svg>
  </div>

  <div class="panel panel--navy">
    <h2 class="locations__title">LOCATIONS</h2>
    <div class="location"><svg viewBox="0 0 20 26"><path d="M10 0a9 9 0 0 0-9 9c0 7 9 17 9 17s9-10 9-17a9 9 0 0 0-9-9z" fill="var(--orange)"/><circle cx="10" cy="9" r="3.5" fill="var(--navy)"/></svg><div class="location__addr">212 Alder Row<br>Webster Groves, MO 63119<br><span class="location__phone">(314) 555-0142</span></div></div>
    <div class="location"><svg viewBox="0 0 20 26"><path d="M10 0a9 9 0 0 0-9 9c0 7 9 17 9 17s9-10 9-17a9 9 0 0 0-9-9z" fill="var(--orange)"/><circle cx="10" cy="9" r="3.5" fill="var(--navy)"/></svg><div class="location__addr">Larkin Medical Center<br>480 Bellwood Place, #120<br>St. Louis, MO 63110<br><span class="location__phone">(314) 555-0167</span></div></div>
    <div class="location"><svg viewBox="0 0 20 26"><path d="M10 0a9 9 0 0 0-9 9c0 7 9 17 9 17s9-10 9-17a9 9 0 0 0-9-9z" fill="var(--orange)"/><circle cx="10" cy="9" r="3.5" fill="var(--navy)"/></svg><div class="location__addr">9150 Hollin Court, Suite 140<br>St. Louis, MO 63141<br><span class="location__phone">(314) 555-0189</span></div></div>
    <div class="location"><svg viewBox="0 0 20 26"><path d="M10 0a9 9 0 0 0-9 9c0 7 9 17 9 17s9-10 9-17a9 9 0 0 0-9-9z" fill="var(--orange)"/><circle cx="10" cy="9" r="3.5" fill="var(--navy)"/></svg><div class="location__addr">3318 Tavel Drive, Suite 120<br>Bridgeton, MO 63044<br><span class="location__phone">(314) 555-0123</span></div></div>
    <div class="location"><svg viewBox="0 0 20 26"><path d="M10 0a9 9 0 0 0-9 9c0 7 9 17 9 17s9-10 9-17a9 9 0 0 0-9-9z" fill="var(--orange)"/><circle cx="10" cy="9" r="3.5" fill="var(--navy)"/></svg><div class="location__addr">64 Quarry Lane, Ste 1<br>Fairview Heights, IL 62208<br><span class="location__phone">(618) 555-0176</span></div></div>
  </div>

  <div class="panel cover">
    <div class="cover__brand"><span class="brand__name">Kelvra MedWorks</span></div>
    <div class="cover__band">We Are Making A <em>Difference</em><br>In Peoples Lives</div>
    <div class="cover__photo" role="img" aria-label="Group photo of the prosthetic team smiling together"></div>
    <div class="cover__body">
      <svg class="cover__swoosh" viewBox="0 0 367 60" preserveAspectRatio="none"><path d="M0 40 Q190 0 367 22 V60 H0Z" fill="var(--orange)"/><path d="M0 52 Q190 12 367 34 V60 H0Z" fill="var(--navy-deep)"/></svg>
      <h1 class="cover__title">Meet Our<br><span>Prosthetic</span><br>Team</h1>
      <span class="cover__url">www.kelvramedworks.com</span>
    </div>
  </div>
</section>

<section class="spread spread--inside" aria-label="Brochure inside">
  <div class="panel panel--white">
    <h2 class="why__title">Why use Kelvra MedWorks?</h2>
    <ul class="why__list">
      <li><svg viewBox="0 0 16 16"><circle cx="8" cy="8" r="8" fill="var(--orange)"/><path d="M4 8.5l2.5 2.5L12 5.5" stroke="#fff" stroke-width="2" fill="none"/></svg><span><b>First-class patient care</b> – Our facility is accredited and every clinician is board certified.</span></li>
      <li><svg viewBox="0 0 16 16"><circle cx="8" cy="8" r="8" fill="var(--orange)"/><path d="M4 8.5l2.5 2.5L12 5.5" stroke="#fff" stroke-width="2" fill="none"/></svg><span><b>High-end technology</b> – We stay current on the latest components and materials.</span></li>
      <li><svg viewBox="0 0 16 16"><circle cx="8" cy="8" r="8" fill="var(--orange)"/><path d="M4 8.5l2.5 2.5L12 5.5" stroke="#fff" stroke-width="2" fill="none"/></svg><span><b>Local Fabrication Facility</b> – Our own lab builds and adjusts devices close to home.</span></li>
      <li><svg viewBox="0 0 16 16"><circle cx="8" cy="8" r="8" fill="var(--orange)"/><path d="M4 8.5l2.5 2.5L12 5.5" stroke="#fff" stroke-width="2" fill="none"/></svg><span><b>Experience</b> – Decades of combined prosthetic expertise.</span></li>
      <li><svg viewBox="0 0 16 16"><circle cx="8" cy="8" r="8" fill="var(--orange)"/><path d="M4 8.5l2.5 2.5L12 5.5" stroke="#fff" stroke-width="2" fill="none"/></svg><span><b>Fast turnaround</b> – Quick fittings get patients moving again sooner.</span></li>
      <li><svg viewBox="0 0 16 16"><circle cx="8" cy="8" r="8" fill="var(--orange)"/><path d="M4 8.5l2.5 2.5L12 5.5" stroke="#fff" stroke-width="2" fill="none"/></svg><span><b>A firm belief in teamwork</b> – We work with patients, physicians and therapists together.</span></li>
    </ul>
    <p class="why__summary">All of these combined allow us to provide the best possible outcome</p>
    <div class="callbox">
      <span class="callbox__icon"><svg width="22" height="22" viewBox="0 0 24 24"><path d="M6.6 10.8a15 15 0 0 0 6.6 6.6l2.2-2.2a1 1 0 0 1 1-.25 11.4 11.4 0 0 0 3.6.57 1 1 0 0 1 1 1V20a1 1 0 0 1-1 1A17 17 0 0 1 3 4a1 1 0 0 1 1-1h3.5a1 1 0 0 1 1 1c0 1.25.2 2.45.57 3.57a1 1 0 0 1-.25 1z" fill="#fff"/></svg></span>
      <span class="callbox__text">Call us today for a <b>Free consult</b><br>and <b>Prosthetic Check-up</b></span>
    </div>
    <div class="why__phone">Call: (314) 555-0142</div>
    <svg class="wave" viewBox="0 0 367 110" preserveAspectRatio="none"><path d="M0 30 Q180 0 367 26 V110 H0Z" fill="var(--orange)"/><path d="M0 44 Q180 14 367 40 V110 H0Z" fill="var(--navy)"/></svg>
  </div>

  <div class="panel panel--navy">
    <div class="member"><div><h3 class="member__name">Daniel Rourke, CPO, American Board Certified Prosthetist</h3><p class="member__bio">Daniel has fitted patients for over twenty years and leads our clinical team with a focus on lower limb care.</p></div><div class="member__photo photo" role="img" aria-label="Portrait of Daniel Rourke"></div></div>
    <div class="member member--flip"><div><h3 class="member__name">Marcus Feld, CP, American Board Certified Prosthetist</h3><p class="member__bio">Marcus specializes in upper limb devices and enjoys helping patients return to work and the hobbies they love.</p></div><div class="member__photo photo" role="img" aria-label="Portrait of Marcus Feld"></div></div>
    <div class="member"><div><h3 class="member__name">Jenna Whitcomb, CP, American Board Certified Prosthetist</h3><p class="member__bio">Jenna joined our team after residency and brings a calm, caring approach to every new fitting.</p></div><div class="member__photo photo" role="img" aria-label="Portrait of Jenna Whitcomb"></div></div>
    <div class="member member--flip"><div><h3 class="member__name">Alyssa Corran, CP, American Board Certified Prosthetist</h3><p class="member__bio">Alyssa works closely with therapists to guide patients through gait training and daily adjustments.</p></div><div class="member__photo photo" role="img" aria-label="Portrait of Alyssa Corran"></div></div>
  </div>

  <div class="panel panel--navy">
    <div class="member member--flip"><div><h3 class="member__name">Peter Lund, CPO, American Board Certified Prosthetist</h3><p class="member__bio">Peter has served the region for decades and mentors our newer clinicians in casting and fitting.</p></div><div class="member__photo photo" role="img" aria-label="Portrait of Peter Lund"></div></div>
    <div class="member"><div><h3 class="member__name">Owen Hadley, CP, American Board Certified Prosthetist</h3><p class="member__bio">Owen focuses on active users and sports limbs, helping patients run, hike and play again.</p></div><div class="member__photo photo" role="img" aria-label="Portrait of Owen Hadley"></div></div>
    <div class="member member--flip"><div><h3 class="member__name">Graham Keele, CPO, Certified Prosthetist Orthotist</h3><p class="member__bio">Graham oversees our fabrication lab to ensure each device is built with care and precision.</p></div><div class="member__photo photo" role="img" aria-label="Portrait of Graham Keele"></div></div>
    <h3 class="partner__title">A PARTNER IN THE PROCESS</h3>
    <div class="partner">
      <p>The loss of a limb is the start of a new chapter. Our team walks beside you from the first visit through every follow-up, adjusting your prosthesis as your needs change so you can live with confidence and independence.</p>
      <div class="partner__image photo" role="img" aria-label="Image of a modern lower limb prosthesis"></div>
    </div>
  </div>
</section>

</body>
</html>
```